Commercial Real Estate

We need a business card design for a new commercial real estate business that specializes in apartment building brokerage. Not individual units but the entire complex. We find and represent the owners existing buildings and well as new buyers for those buildings. The design should convey trust, integrity, knowledge and growth. It should be easily read.

Target Market(s)

40 to 65 years old

Industry/Entity Type

Real Estate

```html
<!DOCTYPE html>
<html lang="en">
<head>
<meta charset="utf-8">
<title>Landvale Property Investments – Business Card</title>
<link href="https://fonts.googleapis.com/css2?family=Arimo:wght@400;700&display=swap" rel="stylesheet">
<style>
  :root {
    --backdrop: #2b2b2b;
    --card: #ffffff;
    --teal: #6fcaca;
    --slate: #4b5757;
    --ink: #4a5454;
  }
  * { margin: 0; padding: 0; box-sizing: border-box; }
  html, body {
    width: 1200px;
    height: 1000px;
    overflow: hidden;
    background: var(--backdrop);
    font-family: "Arimo", Arial, sans-serif;
  }
  .card {
    position: absolute;
    left: 150px;
    top: 243px;
    width: 900px;
    height: 514px;
    background: var(--card);
    overflow: hidden;
  }
  .brand {
    position: absolute;
    left: 90px;
    top: 200px;
    width: 300px;
    display: flex;
    align-items: center;
    gap: 14px;
  }
  .brand-square {
    width: 22px;
    height: 22px;
    background: var(--teal);
    flex: none;
  }
  .brand-name {
    color: var(--slate);
    font-weight: 700;
    font-size: 28px;
    line-height: 1.15;
    letter-spacing: 1px;
  }
  .person {
    position: absolute;
    left: 485px;
    top: 95px;
  }
  .person-name {
    color: var(--ink);
    font-weight: 700;
    font-size: 25px;
    letter-spacing: 0.5px;
  }
  .person-role {
    color: var(--teal);
    font-size: 18px;
    margin-top: 2px;
    margin-left: 14px;
  }
  .contacts {
    position: absolute;
    left: 530px;
    top: 185px;
    list-style: none;
  }
  .contacts li {
    display: flex;
    align-items: center;
    gap: 14px;
    color: var(--ink);
    font-size: 19px;
    height: 27px;
  }
  .contacts svg { width: 18px; height: 18px; fill: var(--teal); flex: none; }
  .office {
    position: absolute;
    left: 560px;
    top: 300px;
    font-size: 19px;
    line-height: 1.3;
    color: var(--ink);
  }
  .office-company { color: var(--teal); font-weight: 700; }
  .band-slate {
    position: absolute;
    left: 0;
    bottom: 0;
    width: 560px;
    height: 12px;
    background: var(--slate);
  }
  .band-teal {
    position: absolute;
    left: 568px;
    bottom: 0;
    width: 332px;
    height: 40px;
    background: var(--teal);
  }
</style>
</head>
<body>
  <main class="card">
    <div class="brand">
      <span class="brand-square"></span>
      <span class="brand-name">LANDVALE Property Investments</span>
    </div>

    <div class="person">
      <div class="person-name">YOUR NAME</div>
      <div class="person-role">Director</div>
    </div>

    <ul class="contacts">
      <li>
        <svg viewBox="0 0 24 24" aria-hidden="true"><path d="M6.6 10.8a15 15 0 0 0 6.6 6.6l2.2-2.2a1 1 0 0 1 1-.25 11.4 11.4 0 0 0 3.6.6 1 1 0 0 1 1 1V20a1 1 0 0 1-1 1A17 17 0 0 1 3 4a1 1 0 0 1 1-1h3.5a1 1 0 0 1 1 1c0 1.25.2 2.45.6 3.6a1 1 0 0 1-.25 1z"/></svg>
        555 010 2040
      </li>
      <li>
        <svg viewBox="0 0 24 24" aria-hidden="true"><path d="M7 3h10v5H7zM4 9h16a2 2 0 0 1 2 2v6h-4v4H6v-4H2v-6a2 2 0 0 1 2-2zm4 7v3h8v-3z"/></svg>
        555 010 2040
      </li>
      <li>
        <svg viewBox="0 0 24 24" aria-hidden="true"><path d="M2 5h20v2l-10 6L2 7zm0 4 10 6 10-6v10H2z"/></svg>
        yourname@landvale.com
      </li>
    </ul>

    <div class="office">
      <div class="office-company">LANDVALE Property Investments</div>
      <div>Suite 45 Hollins Road,</div>
      <div>Westbury 54321</div>
    </div>

    <div class="band-slate"></div>
    <div class="band-teal"></div>
  </main>
</body>
</html>
```